business card for law firm that reflects the web site -www.MarenHolt.com. That is pleasant to read

We need a business card for a small law firm. Your company designed our logo - tree of life - which I can provide to the designers. The card should be on both sides. Use the coloring from the web site (www.MarenHolt.com) and logo (I have several formats). I am attaching the logo, but not sure what format to use.

First side name of firm: Law Office of M.K. Holt, P.A. 4816 West Sorrelwood, Suite 300, Phoenix, AZ 85019, Phone: 602.555.0143, Fax: 602.555.0187, web site: www.MarenHolt.com, email: MHolt@MarenHolt.com.
Maren K. Holt Bankruptcy and Foreclosure Attorney & Counselor.
Back side (perhaps vertical) the logo and then Notes with lines. At the bottom: Proud to help people and small businesses file for bankruptcy protection. We are a debt relief agency.
Updates

I have several versions of the logo. Will be happy to share whatever you need. Added Sunday, April 3, 2016

Target Market(s)

everyone

Industry/Entity Type

Legal

Contact Information for Business Card

I prefer something unique (rounded edges, design that adopts my web site - www.MarenHolt.com.

Font styles to use
Serif

Requirements
Must have
• First side name of firm: Law Office of M.K. Holt, P.A. 4816 West Sorrelwood, Suite 300, Phoenix, AZ 85019, Phone: 602.555.0143, Fax: 602.555.0187, web site: www.MarenHolt.com, email: MHolt@MarenHolt.com.
• Maren K. Holt Bankruptcy and Foreclosure Attorney & Counselor.
• Back side (perhaps vertical) the logo and then Notes with lines. At the bottom: Proud to help people and small businesses file for bankruptcy protection. We are a debt relief agency.
• Green and brown colors that reflect the web site: www.MarenHolt.com
Should not have
• Type so small that older people cannot read.

```html
<!DOCTYPE html>
<html lang="en">
<head>
<meta charset="utf-8">
<title>Law Office of M.K. Holt, P.A. — Business Card</title>
<link href="https://fonts.googleapis.com/css2?family=Tinos:ital,wght@0,400;0,700;1,400&display=swap" rel="stylesheet">
<style>
  :root {
    --stage: #e9e6e1;
    --card: #fbfbfa;
    --card-edge: #e2e1de;
    --brown: #4a2617;
    --brown-line: #7a3b22;
    --green: #2f5a32;
    --green-dark: #1f4424;
    --ink: #2a2623;
    --rule: #3b3531;
  }
  * { box-sizing: border-box; margin: 0; padding: 0; }
  html, body { width: 1200px; height: 780px; overflow: hidden; }
  body {
    background: var(--stage);
    font-family: "Tinos", "Times New Roman", serif;
    color: var(--ink);
    position: relative;
  }
  .card {
    position: absolute;
    top: 235px;
    width: 540px;
    height: 310px;
    background: radial-gradient(ellipse at 55% 40%, #ffffff 0%, var(--card) 60%, #f1f1ef 100%);
    border: 1px solid var(--card-edge);
    border-radius: 18px;
    box-shadow: 0 3px 10px rgba(0,0,0,0.12);
    overflow: hidden;
  }
  .card--front { left: 40px; }
  .card--back  { left: 620px; }

  /* Front */
  .firm-mark {
    position: absolute;
    left: 30px; top: 40px;
    width: 76px; height: 76px;
    border-radius: 50%;
    background: var(--green);
    box-shadow: 0 0 0 5px #6b3a26;
  }
  .firm-heading {
    position: absolute; left: 124px; top: 30px; color: var(--brown);
    white-space: nowrap;
  }
  .firm-heading__pre {
    font-size: 17px; font-weight: 700; letter-spacing: 1px; text-transform: uppercase;
    line-height: 1.2;
  }
  .firm-heading__name {
    font-size: 42px; font-weight: 700; line-height: 1.1; letter-spacing: 0.5px;
  }
  .firm-heading__suffix { font-size: 20px; letter-spacing: 1px; }
  .attorney {
    position: absolute; right: 26px; top: 104px; text-align: right; color: var(--brown);
    white-space: nowrap;
  }
  .attorney__name {
    font-size: 19px; font-weight: 700; letter-spacing: 1px; text-transform: uppercase;
    line-height: 1.2;
  }
  .title-rule {
    position: absolute; left: 30px; right: 26px; top: 131px;
    height: 1px; background: var(--brown-line);
  }
  .attorney__role {
    position: absolute; right: 26px; top: 137px;
    font-size: 15.5px; color: var(--green); white-space: nowrap;
  }
  .contact {
    position: absolute; left: 30px; bottom: 24px;
    list-style: none; font-size: 15px; color: var(--ink); line-height: 1.35;
  }
  .contact__item { display: flex; align-items: center; gap: 8px; }
  .contact__icon { width: 13px; height: 13px; flex: none; }
  .address {
    position: absolute; right: 26px; top: 180px; text-align: right;
    font-size: 15.5px; color: var(--brown); line-height: 1.35; font-style: normal;
  }

  /* Back */
  .note-title {
    position: absolute; top: 24px; left: 0; right: 0; text-align: center;
    font-size: 17px; letter-spacing: 1px; color: var(--ink);
  }
  .note-lines {
    position: absolute; left: 40px; right: 40px; top: 56px; list-style: none;
  }
  .note-lines li { height: 30px; border-bottom: 1px solid var(--rule); }
  .back-footer {
    position: absolute; left: 0; right: 0; bottom: 22px; text-align: center;
    font-size: 15px; font-style: italic; color: var(--ink); line-height: 1.35;
  }
  .back-footer__web { font-weight: 700; font-style: italic; color: var(--ink); }
</style>
</head>
<body>

<section class="card card--front" aria-label="Business card front">
  <div class="firm-mark" aria-hidden="true"></div>

  <header class="firm-heading">
    <div class="firm-heading__pre">Law Office of</div>
    <div class="firm-heading__name">M.K. HOLT<span class="firm-heading__suffix">, P.A</span></div>
  </header>

  <div class="attorney"><div class="attorney__name">Maren K. Holt</div></div>
  <div class="title-rule"></div>
  <div class="attorney__role">Bankruptcy and Foreclosure Attorney &amp; Counselor</div>

  <address class="address">
    4816 West Sorrelwood<br>
    Suite 300, Phoenix, AZ 85019
  </address>

  <ul class="contact">
    <li class="contact__item">
      <svg class="contact__icon" viewBox="0 0 13 13" aria-label="Phone"><rect width="13" height="13" rx="1.5" fill="var(--green-dark)"/><path d="M4 3l1.5 0 .6 2-1 .7c.5 1 1.2 1.7 2.2 2.2l.7-1 2 .6V10c-3.5 0-6-2.5-6-6z" fill="#fff"/></svg>
      602.555.0143
    </li>
    <li class="contact__item">
      <svg class="contact__icon" viewBox="0 0 13 13" aria-label="Fax"><rect width="13" height="13" rx="1.5" fill="var(--green-dark)"/><rect x="3" y="5" width="7" height="4.5" fill="#fff"/><rect x="4.2" y="2.8" width="4.6" height="2.4" fill="#fff"/></svg>
      602.555.0187
    </li>
    <li class="contact__item">
      <svg class="contact__icon" viewBox="0 0 13 13" aria-label="Email"><rect width="13" height="13" rx="1.5" fill="var(--green-dark)"/><rect x="2.5" y="3.8" width="8" height="5.4" fill="#fff"/><path d="M2.5 3.8l4 3 4-3" stroke="var(--green-dark)" stroke-width="0.9" fill="none"/></svg>
      MHolt@MarenHolt.com
    </li>
  </ul>
</section>

<section class="card card--back" aria-label="Business card back">
  <h2 class="note-title">NOTE</h2>
  <ul class="note-lines" aria-hidden="true">
    <li></li><li></li><li></li><li></li><li></li>
  </ul>
  <p class="back-footer">
    Proud to help people and small businesses file for bankruptcy protection.<br>
    We are a debt relief agency.<br>
    <span class="back-footer__web">www.MarenHolt.com</span>
  </p>
</section>

</body>
</html>
```